Broschüren-Design für Versicherungsagenten
Zielgruppe
Ich bin mit KL-Vorsorge als unabhängiger Versicherungsagent Selbstständig. (www.kl-vorsorge.de)
Ich habe mich auf die Absicherung von biometrischen Risiken spezialisiert - die auch in der Broschüre Thematisiert werden sollen. Das Oberthema der Broschüre ist 'biometrische Risiken'. Dies soll dann auf die Themen: Arbeitskraft, Langlebigkeit und Pflege heruntergebrochen werden.
Zielgruppe sind vor allem junge Menschen, die gerade erst eine Ausbildung gestartet oder ihr Studium beendet haben.
Aufgabenstellung
Das Design sollte die drei Hauptbereiche: Arbeitskraft, Langlebigkeit und Pflege, leicht verständlich dem Kunden veranschaulichen. Texte, Informationen und Grafiken (in der Reihenfolge, so wie ich mir das vorstelle) sind als Datei beigefügt.
Das ganze soll im DIN A4 Format gedruckt werden, wobei ich auf einen Hochwertigen Druck inklusive Druckveredelung hohen Wert lege.

```html
<!DOCTYPE html>
<html lang="de">
<head>
<meta charset="utf-8">
<title>KL-Vorsorge – Biometrische Risikoabsicherung</title>
<link href="https://fonts.googleapis.com/css2?family=Open+Sans:ital,wght@0,400;0,600;0,700;0,800;1,400&display=swap" rel="stylesheet">
<style>
:root{
  --stage:#dcdcdd;
  --paper:#f4f4f4;
  --ink:#1f1f1f;
  --grey:#8a8a8a;
  --red:#cf2a52;
  --panel-blue:#dde9f2;
  --sky:#7cc6ea;
  --teal:#41bccb;
  --blue:#2a8ccf;
  --yellow:#f3d11f;
  --dark-bar:#333;
}
*{margin:0;padding:0;box-sizing:border-box}
html,body{width:1200px;height:2397px;overflow:hidden}
body{background:var(--stage);font-family:"Open Sans",Arial,sans-serif;color:var(--ink);position:relative}
.abs{position:absolute}
.page{position:absolute;background:var(--paper);overflow:hidden}

/* ---------- Cover ---------- */
.cover{left:390px;top:100px;width:420px;height:594px;box-shadow:0 10px 24px rgba(0,0,0,.18)}
.cover-photo{left:0;top:0;width:420px;height:300px;
  background:linear-gradient(160deg,#e8e8e8 0,#9a9a9a 45%,#5a6470 70%,#d4d4d4 100%)}
.brand{left:270px;top:18px;display:flex;align-items:center;gap:7px;font-weight:700;font-size:16px;color:var(--ink)}
.brand-dot{width:22px;height:22px;border-radius:50%;background:var(--ink)}
.cover-badge{left:300px;top:250px;width:92px;height:92px;border-radius:50%;background:var(--red);color:#fff;
  font-weight:700;font-size:12px;line-height:1.2;display:flex;align-items:center;justify-content:center;text-align:center;text-transform:uppercase}
.cover-title{left:40px;top:345px;color:var(--red);font-weight:800;font-size:29px;line-height:1.05;text-transform:uppercase}
.cover-lead{left:40px;top:425px;width:200px;font-size:9px;line-height:1.45;color:var(--grey)}
.cover-foot{left:0;top:544px;width:420px;height:50px;background:#e9e9e9}

/* ---------- Spread 1 ---------- */
.spread{position:absolute;box-shadow:0 10px 26px rgba(0,0,0,.18)}
.spread-one{left:100px;top:850px;width:1000px;height:700px}
.gutter{top:0;width:40px;height:100%;background:linear-gradient(90deg,transparent,rgba(0,0,0,.08),transparent)}
.intro-head{left:160px;top:42px;width:170px}
.intro-head h2{font-size:11px;font-weight:800;line-height:1.15;text-transform:uppercase}
.intro-head p{font-size:7.5px;line-height:1.4;margin-top:6px;color:#444}
.intro-head .lead-bold{font-weight:700;font-style:italic;color:var(--ink)}
.toc{left:100px;top:390px;width:200px}
.toc h3{font-size:14px;font-weight:800;letter-spacing:.5px;margin-bottom:10px}
.toc li{list-style:none;display:flex;gap:22px;font-size:8px;text-transform:uppercase;color:#444;line-height:2;white-space:nowrap}
.toc li span{width:10px;text-align:right}
.couple-photo{left:345px;top:110px;width:335px;height:590px;border-radius:168px 168px 0 0;
  background:linear-gradient(180deg,#e9e6e3 0,#d8ccc2 22%,#bfbfbf 38%,#9fb4cc 62%,#5f7fa6 82%,#3d5d86 100%)}
.life-panel{left:500px;top:150px;width:500px;height:450px;background:var(--panel-blue);clip-path:polygon(48% 0,100% 0,100% 100%,0 100%,0 55%)}
.life-title{left:800px;top:110px;font-size:44px;font-weight:800;line-height:.95;text-transform:uppercase}
.pillar{font-size:8px;line-height:1.35;color:#555;width:115px}
.pillar b{display:block;font-size:11px;font-weight:800;text-transform:uppercase;letter-spacing:.3px}
.pillar-work{left:690px;top:320px;text-align:right}
.pillar-work b{color:var(--sky)}
.pillar-care{left:840px;top:270px}
.pillar-care b{color:var(--teal)}
.pillar-age{left:880px;top:400px}
.pillar-age b{color:var(--blue)}
.life-cube{left:808px;top:325px}
.life-text{left:700px;top:500px;width:270px;font-size:8.5px;line-height:1.5;color:#333;text-align:right}
.life-text p+p{margin-top:6px}

/* ---------- Spread 2 ---------- */
.spread-two{left:60px;top:1630px;width:1080px;height:740px}
.pg-left{left:0;top:0;width:540px;height:740px}
.pg-right{left:540px;top:0;width:540px;height:740px}
.worker-illu{left:60px;top:40px;width:160px;height:110px;border-radius:6px;background:linear-gradient(135deg,#cfe7f5,#9fd0ec 60%,#f3d11f 100%);opacity:.85}
.work-title{left:250px;top:44px;font-size:28px;font-weight:800;text-transform:uppercase;letter-spacing:.5px}
.work-band{left:255px;top:86px;width:220px;height:42px;background:var(--sky);color:#fff;font-size:13px;line-height:1.05;padding:5px 0 0 40px;text-transform:uppercase}
.rule{left:40px;top:150px;width:460px;height:1px;background:#555}
.rule-q{left:150px;top:156px;font-size:8.5px;font-style:italic;color:#333}
.quarter-note{left:350px;top:175px;width:150px;font-size:7.5px;line-height:1.35;color:#444}
.bg-photo{left:0;top:200px;width:330px;height:540px;background:linear-gradient(160deg,#e7eef3,#cfd9e2 50%,#eef1f3);opacity:.9}
.value-band{left:0;top:205px;width:320px;height:22px;background:var(--yellow);font-size:9px;font-weight:700;font-style:italic;padding:4px 0 0 30px}
.value-band b{font-size:13px;font-weight:800;font-style:normal;margin-left:20px}
.formula{left:70px;top:234px;display:flex;gap:6px;font-size:7.5px;font-weight:700}
.formula span{background:var(--sky);color:#fff;padding:3px 8px}
.formula span.x{background:none;color:#333;padding:3px 0}
.million{left:360px;top:240px;font-size:24px;font-weight:800}
.million-note{left:360px;top:276px;width:140px;font-size:7.5px;line-height:1.35;color:#444}
.cause-title{left:30px;top:290px;font-size:20px;font-weight:800;line-height:1;color:#333}
.causes{left:30px;top:360px;width:330px}
.cause{display:flex;align-items:center;height:28px}
.cause-bar{height:14px;font-size:7px;color:#fff;padding:2px 6px;white-space:nowrap;overflow:hidden}
.cause-bar.light{background:var(--sky)}
.cause-bar.dark{background:var(--dark-bar)}
.cause-val{font-size:11px;font-weight:800;margin-left:6px}
.load-bubble{left:370px;top:440px;width:104px;height:104px;border-radius:50%;background:var(--yellow);
  font-size:10px;font-weight:800;font-style:italic;text-align:center;display:flex;align-items:center;justify-content:center;line-height:1.2}
.folio{font-size:7px;color:#777}
.folio-left{left:30px;top:716px}
.folio-right{right:30px;top:716px}

.clock{left:20px;top:25px}
.ability-band{left:100px;top:70px;width:130px;height:310px;background:var(--yellow)}
.ability-head{left:110px;top:80px;width:115px;font-size:10px;font-weight:800;font-style:italic;line-height:1.15}
.ability{display:flex;align-items:flex-start;gap:8px;left:40px;width:190px}
.ability-time{width:34px;font-size:12px;font-weight:800;text-align:right}
.ability-time small{display:block;font-size:6px;font-weight:400}
.ability-txt{font-size:8.5px;font-weight:800;line-height:1.15}
.ability-txt small{display:block;font-weight:400;font-size:7px;color:#333}
.state-title{left:320px;top:60px;font-size:20px;font-weight:800;line-height:1.05}
.state-icon{left:270px;top:64px}
.state-text{left:270px;top:120px;width:220px;font-size:7.5px;line-height:1.4;color:#333}
.state-text p+p{margin-top:5px}
.state-text b{font-weight:700;color:var(--ink)}
.person-illu{left:420px;top:400px;width:70px;height:110px;border-radius:35px 35px 6px 6px;background:linear-gradient(180deg,#e9d8b8,#8a7a6a 40%,#333)}
.gap-note{left:330px;top:470px;width:85px;font-size:9px;font-weight:800;font-style:italic;line-height:1.2}
.income{left:40px;top:400px;width:290px}
.income-row{display:flex;align-items:center;height:22px;font-size:7.5px;white-space:nowrap}
.income-row .lbl{width:90px;color:#333}
.income-row .bar{height:14px;color:#fff;font-weight:700;font-size:7.5px;padding:1px 6px;text-align:right}
.income-row .tag{margin-left:6px;font-weight:700;font-size:8px}
.income-row .bar.sky{background:var(--blue)}
.income-row .bar.dark{background:var(--dark-bar)}
.keep-q{left:40px;top:545px;width:170px;font-size:10px;font-weight:800;font-style:italic;line-height:1.15}
.gap-chart{left:40px;top:600px;width:360px}
.gap-row{display:flex;align-items:center;height:22px;font-size:7.5px}
.gap-row .lbl{width:90px;color:#333}
.gap-row .seg{height:14px;font-size:7.5px;font-weight:700;padding:1px 5px;text-align:right}
.seg.dark{background:var(--dark-bar);color:#fff}
.seg.yellow{background:var(--yellow)}
.footnote{left:40px;top:690px;width:440px;font-size:6.5px;color:#555}
</style>
</head>
<body>

<section class="page cover" aria-label="Titelseite">
  <div class="abs cover-photo" role="img" aria-label="Foto: Nahaufnahme eines Auges mit Erdkugel in der Iris, umgeben von Binärzahlen"></div>
  <div class="abs brand"><span class="brand-dot"></span>KL-Vorsorge</div>
  <div class="abs cover-badge">Jetzt<br>absichern!</div>
  <h1 class="abs cover-title">Biometrische<br>Risikoabsicherung</h1>
  <p class="abs cover-lead">Menschen sind bisher nur unzureichend über das große Potenzial der biometrischen Risiken und ihrer existenzbedrohenden Folgen aufgeklärt.</p>
  <div class="abs cover-foot"></div>
</section>

<section class="spread spread-one" aria-label="Doppelseite Ihr Leben">
  <div class="page" style="left:0;top:0;width:500px;height:700px;background:#f1f1f1"></div>
  <div class="page" style="left:500px;top:0;width:500px;height:700px"></div>
  <div class="abs gutter" style="left:480px"></div>

  <div class="abs intro-head">
    <h2>Biometrische<br>Risiko-<br>absicherung</h2>
    <p>In einer modernen Welt – die immer schneller zusammenwächst – sind Spezialisten gefragt.</p>
    <p>Wir sind Ihr Spezialist auf dem Gebiet der biometrischen Risikoabsicherung.</p>
    <p class="lead-bold">Biometrische Risiken werden die Risiken genannt, die unmittelbar mit Ihrem Leben verknüpft sind.</p>
  </div>

  <div class="abs toc">
    <h3>INHALT</h3>
    <ul>
      <li><span>3</span>Ihr Leben</li>
      <li><span>4</span>Arbeitskraft</li>
      <li><span>7</span>Langlebigkeit</li>
      <li><span>11</span>Pflegebedürftigkeit</li>
      <li><span>14</span>Über uns</li>
    </ul>
  </div>

  <div class="abs life-panel"></div>
  <div class="abs couple-photo" role="img" aria-label="Foto: junges Paar in Jeans und Shirt, Arm in Arm"></div>
  <h2 class="abs life-title">Ihr<br>Leben</h2>

  <div class="abs pillar pillar-work"><b>Arbeitskraft</b>Haben Sie ohne Arbeitskraft noch ein Einkommen?</div>
  <div class="abs pillar pillar-care"><b>Pflege</b>Können Sie Ihr tägliches Leben noch selbst bewältigen?</div>
  <div class="abs pillar pillar-age"><b>Langlebigkeit</b>Können Sie sich alt werden auch finanziell leisten?</div>
  <svg class="abs life-cube" width="80" height="76" viewBox="0 0 80 76" aria-hidden="true">
    <polygon points="40,4 76,20 40,36 4,20" fill="#8fdbe6"/>
    <polygon points="4,20 40,36 40,72 4,56" fill="#b6e3f3"/>
    <polygon points="76,20 40,36 40,72 76,56" fill="#2a8ccf"/>
  </svg>

  <div class="abs life-text">
    <p>Viele Menschen sind bisher nur unzureichend über das große Potenzial dieser Risiken und vor allem ihrer existenzbedrohenden Folgen aufgeklärt.</p>
    <p>Vorzugsweise junge Leute, die sich kostengünstig absichern könnten, erkennen häufig auch noch nicht die Notwendigkeit einer solchen Absicherung.</p>
    <p>Auf den nachfolgenden Seiten finden Sie einige Erläuterungen zu den wichtigsten Aspekten in der Absicherung von biometrischen Risiken.</p>
  </div>
</section>

<section class="spread spread-two" aria-label="Doppelseite Arbeitskraft">
  <div class="page pg-left">
    <div class="abs worker-illu" role="img" aria-label="Illustration: Arbeiter mit Münzen und vier Figuren mit Helmen"></div>
    <h2 class="abs work-title">Arbeitskraft</h2>
    <div class="abs work-band">Ihr größtes<br>Vermögen</div>
    <div class="abs rule"></div>
    <p class="abs rule-q">Können Sie wissen, ob Sie einer der anderen drei oder der/die EINE sind?</p>
    <p class="abs quarter-note">Einer von vier Menschen kann im Laufe seines Lebens seinen ursprünglichen Beruf aus gesundheitlichen Gründen nicht mehr ausüben!</p>

    <div class="abs bg-photo" role="img" aria-label="Blasses Hintergrundfoto einer Arbeitssituation"></div>
    <div class="abs value-band">Wie viel ist Ihre Arbeitskraft <b>WERT ?</b></div>
    <div class="abs formula"><span>Einkommen</span><span class="x">×</span><span>12</span><span class="x">×</span><span>Arbeitsjahre</span></div>
    <div class="abs million">1.500.000 €</div>
    <p class="abs million-note">Im Laufe eines Arbeitslebens verdient ein durchschnittlicher Erwerbstätiger rund 1,5 Millionen Euro!</p>

    <h3 class="abs cause-title">Ursachen für den<br>Verlust der<br>Arbeitskraft</h3>
    <div class="abs causes">
      <div class="cause"><div class="cause-bar light" style="width:60px">Unfälle</div><span class="cause-val">7 %</span></div>
      <div class="cause"><div class="cause-bar dark" style="width:110px">Herz- und Gefäßerkrankungen</div><span class="cause-val">9 %</span></div>
      <div class="cause"><div class="cause-bar light" style="width:150px">Krebs / andere bösartige Geschwülste</div><span class="cause-val">15 %</span></div>
      <div class="cause"><div class="cause-bar dark" style="width:200px">Erkrankungen des Skeletts und Bewegungsapparates</div><span class="cause-val">21 %</span></div>
      <div class="cause"><div class="cause-bar light" style="width:280px">Nerven und andere psychische Erkrankungen</div><span class="cause-val">32 %</span></div>
      <div class="cause"><div class="cause-bar dark" style="width:145px">sonstige Erkrankungen</div><span class="cause-val">16 %</span></div>
    </div>
    <div class="abs load-bubble">Welchen<br>Belastungen sind<br>Sie ausgesetzt?</div>
    <div class="abs folio folio-left">4 Biometrische Risikoabsicherung</div>
  </div>

  <div class="page pg-right">
    <svg class="abs clock" width="80" height="80" viewBox="0 0 80 80" aria-hidden="true">
      <circle cx="40" cy="40" r="38" fill="#7cc6ea"/>
      <circle cx="40" cy="40" r="32" fill="#222"/>
      <line x1="40" y1="40" x2="40" y2="18" stroke="#fff" stroke-width="3"/>
      <line x1="40" y1="40" x2="56" y2="48" stroke="#fff" stroke-width="2"/>
    </svg>
    <div class="abs ability-band"></div>
    <p class="abs ability-head">Tägliche Arbeitsfähigkeit in irgendeiner Tätigkeit:</p>

    <div class="abs ability" style="top:160px">
      <div class="ability-time"><small>weniger als</small>3h</div>
      <svg width="26" height="26" viewBox="0 0 26 26"><circle cx="13" cy="13" r="12" fill="#fff" stroke="#222"/><path d="M13 13 L13 1 A12 12 0 0 1 25 13 Z" fill="#222"/></svg>
      <div class="ability-txt">Volle Erwerbsminderungsrente<small>ca. 30 – 35 % vom Bruttoeinkommen</small></div>
    </div>
    <div class="abs ability" style="top:230px">
      <div class="ability-time">3-6h</div>
      <svg width="26" height="26" viewBox="0 0 26 26"><circle cx="13" cy="13" r="12" fill="#fff" stroke="#222"/><path d="M13 13 L13 1 A12 12 0 0 1 13 25 Z" fill="#222"/></svg>
      <div class="ability-txt">Halbe Erwerbsminderungsrente<small>ca. 15 – 17,5 % vom Bruttoeinkommen</small></div>
    </div>
    <div class="abs ability" style="top:300px">
      <div class="ability-time">6h+</div>
      <svg width="26" height="26" viewBox="0 0 26 26"><circle cx="13" cy="13" r="12" fill="#222"/></svg>
      <div class="ability-txt">Keine Leistungen mehr</div>
    </div>

    <svg class="abs state-icon" width="40" height="40" viewBox="0 0 40 40" aria-hidden="true">
      <rect x="3" y="6" width="34" height="30" fill="none" stroke="#222" stroke-width="2"/>
      <line x1="3" y1="13" x2="37" y2="13" stroke="#222" stroke-width="2"/>
      <circle cx="20" cy="26" r="6" fill="none" stroke="#2a8ccf" stroke-width="2"/>
    </svg>
    <h2 class="abs state-title">Staatliche<br>Versorgung</h2>
    <div class="abs state-text">
      <p>Wer aus gesundheitlichen Gründen nicht mehr in der Lage ist, zu arbeiten, wird vom Staat aufgefangen. <b>Volle bzw. halbe Erwerbsminderungsrente</b>.</p>
      <p>Ob halbe oder volle Erwerbsminderungsrente entscheidet sich anhand der verbliebenen Restarbeitsfähigkeit. Der <b>bisherige Beruf</b> ist dabei grundsätzlich <b>unberücksichtigt</b>.</p>
      <p>Sie werden also ohne Rücksicht auf Status, Qualifikation und Zumutbarkeit auf irgendeine Tätigkeit des allgemeinen Arbeitsmarktes hingewiesen.</p>
      <p>Es gibt einen steigenden Bedarf und gleichzeitig eine mangelnde staatliche Unterstützung. Für jeden, der einen Beruf ausübt, ist es also existenziell, Ihrer Versorgungslücke zu treffen.</p>
    </div>
    <div class="abs person-illu" role="img" aria-label="Illustration: besorgte Person mit Gedankenblase voller Geld"></div>
    <p class="abs gap-note">Diese Versorgungslücke bedroht Ihre Existenz.</p>

    <div class="abs income">
      <div class="income-row"><span class="lbl">Arbeitsunfähigkeit</span><div class="bar sky" style="width:130px">3091 €</div><span class="tag" style="color:var(--blue)">Bruttoeinkommen</span></div>
      <div class="income-row"><span class="lbl">nach 7 Wochen</span><div class="bar dark" style="width:100px">2009 €</div><span class="tag">Lohnfortzahlung</span></div>
      <div class="income-row"><span class="lbl">nach 18 Monaten</span><div class="bar dark" style="width:90px">1808 €</div><span class="tag">Krankengeld*</span></div>
      <div class="income-row"><span class="lbl"></span><div class="bar dark" style="width:50px">927 €</div><span class="tag">Volle Erwerbsminderungsrente</span></div>
      <div class="income-row"><span class="lbl"></span><div class="bar dark" style="width:30px">464</div><span class="tag">oder Halbe Erwerbsminderungsrente</span></div>
    </div>
    <p class="abs keep-q">Können Sie weiterhin Ihren hart erarbeiteten Lebensstandard halten?</p>
    <div class="abs gap-chart">
      <div class="gap-row"><span class="lbl">Versorgungslücke</span><div class="seg dark" style="width:50px">927 €</div><div class="seg yellow" style="width:60px">1082 €</div></div>
      <div class="gap-row"><span class="lbl">Beispiel Arbeitsunfähigkeit</span><div class="seg dark" style="width:30px">464 €</div><div class="seg yellow" style="width:80px">1545 €</div></div>
    </div>
    <p class="abs footnote">* Gesetzliches Krankengeld: 70 % des letzten Bruttoeinkommens oder 90 % des letzten Nettoeinkommens.</p>
    <div class="abs folio folio-right">Biometrische Risikoabsicherung 5</div>
  </div>
  <div class="abs gutter" style="left:520px"></div>
</section>

</body>
</html>
```